eco friendly packagin cat litter

I would like to purchase a customized version of a design you have previously submitted - https://www.pixelvane-example.com/design/58820417<br/><br/>we look for a graphic for a pack of litter pellets for cats (and small rodents), the indications of the icons are fine as the example mock-up, we just have to add the possibility of disposing in the toilet!All entries must be in Italian, the product will be called TOVA NIBLO - the subtitle will be "ecological litter for cats and small rodents" LETTIERA ECOLOGICA PER GATTI E PICCOLI RODITORII would like the main image to be of the cat, but I would like the icons to show also rabbits and hamsters.how can I intervene on the texts to give you a hand?I'd like to have a transparent window (not at the base) where you can see the wood pellet.you can see the dimensions from the pen drawing.the Foravia Nordic logo, is the name of our company. I would like it to be present in the pack but not too big.I like the atmosphere of your example pack but I also like the one in the attached photo "RIVO MOSS BEDDING"
Target Market(s)
supermarket and pet food stores
Requirements
Must have
- -a cat
- -eco friendly - aspect
- -a transparent window to show the wood pellets
- -an icon list for product qualities
- -high absorbency (Alto potere assorbente)
- eliminates odors (elimina gli odori)
- 100% natural / ecological (100% naturale)
- cheap- (economico)
- -long time (lunga durata)
- does not stick to the legs (non si attacca alle zampe)
- - a "TOVA NIBLO" international looking logo
- Must be in Italian language

```html
<!DOCTYPE html>
<html lang="it">
<head>
<meta charset="utf-8">
<title>TOVA NIBLO – Lettiera ecologica, varianti A e B</title>
<link rel="stylesheet" href="https://fonts.googleapis.com/css2?family=Fredoka:wght@500;700&family=Roboto:wght@400;700&display=swap">
<style>
  :root {
    --stage: #d9d9d9;
    --bag-green: #7ab833;
    --bag-green-dark: #5f9a22;
    --handle: #8cc83f;
    --brand-red: #e31e24;
    --panel-black: #101010;
    --text-green: #8cc63f;
    --badge-green: #2e8b2e;
    --white: #ffffff;
    --pellet-light: #c9a66b;
    --pellet-dark: #6e5230;
    --photo-light: #b9d46a;
    --photo-mid: #7fa640;
    --photo-dark: #4f7a2a;
    --cat-grey: #9a9a94;
  }
  * { box-sizing: border-box; margin: 0; padding: 0; }
  html, body { width: 1200px; height: 899px; overflow: hidden; }
  body { background: var(--stage); position: relative; font-family: "Roboto", Arial, sans-serif; }

  .variant-label {
    position: absolute; top: 22px;
    font: 700 26px "Roboto", Arial, sans-serif; color: #111;
  }
  .variant-label--a { left: 120px; }
  .variant-label--b { left: 700px; }

  .bag {
    position: absolute; top: 72px; width: 468px; height: 792px;
    border-radius: 10px 10px 6px 6px; overflow: hidden;
    background: var(--bag-green);
  }
  .bag--a { left: 96px; }
  .bag--b { left: 668px; }

  .bag__top {
    position: absolute; left: 0; top: 0; width: 100%; height: 150px;
    background: linear-gradient(180deg, #86c43c, var(--bag-green-dark));
  }
  .bag__handle {
    position: absolute; left: 144px; top: 42px; width: 174px; height: 66px;
    border-radius: 40px 40px 80px 80px / 20px 20px 46px 46px;
    background: linear-gradient(180deg, #98d04d, var(--handle));
    box-shadow: inset 0 -6px 10px rgba(0,0,0,.12);
  }

  .bag__photo {
    position: absolute; left: 0; top: 150px; width: 100%; height: 556px;
    background:
      radial-gradient(ellipse 38% 55% at 78% 55%, var(--cat-grey) 0%, rgba(154,154,148,.7) 45%, rgba(154,154,148,0) 75%),
      linear-gradient(160deg, var(--photo-light) 0%, var(--photo-mid) 55%, var(--photo-dark) 100%);
  }

  .brand-panel {
    position: absolute; left: 36px; top: 152px; width: 200px; height: 232px;
    background: var(--brand-red);
    display: flex; align-items: flex-end; justify-content: center; padding-bottom: 36px;
  }
  .brand-name {
    font: 700 40px/0.95 "Fredoka", Arial, sans-serif; color: var(--white);
    text-align: center; letter-spacing: 1px;
  }

  .claim-panel {
    position: absolute; left: 36px; top: 384px; width: 200px; height: 120px;
    background: var(--panel-black); color: var(--text-green);
    text-align: center; padding-top: 12px;
  }
  .claim-panel__title { font: 700 22px/1.08 "Fredoka", Arial, sans-serif; letter-spacing: .5px; }
  .claim-panel__sub { font: 500 18px/1.2 "Fredoka", Arial, sans-serif; margin-top: 2px; }

  .natural-badge { position: absolute; left: 50px; top: 520px; width: 180px; height: 66px; }

  .pellet-window {
    position: absolute; left: 38px; top: 598px; width: 200px; height: 92px;
    border-radius: 8px;
    background:
      radial-gradient(circle at 20% 30%, var(--pellet-light) 0 8px, transparent 9px),
      radial-gradient(circle at 55% 60%, var(--pellet-light) 0 8px, transparent 9px),
      radial-gradient(circle at 82% 35%, var(--pellet-light) 0 8px, transparent 9px),
      linear-gradient(135deg, #a8814a, var(--pellet-dark));
    box-shadow: inset 0 0 0 2px rgba(255,255,255,.25);
  }

  .feature-band {
    position: absolute; left: 0; top: 706px; width: 100%; height: 86px;
    background: var(--panel-black);
  }
  .feature-list {
    position: absolute; left: 14px; top: 10px; width: 330px;
    display: flex; list-style: none;
  }
  .feature {
    flex: 1 1 0; text-align: center; color: var(--white);
    font: 400 7px/1.15 "Roboto", Arial, sans-serif;
    border-right: 1px solid rgba(255,255,255,.55); padding: 0 2px;
  }
  .feature:last-child { border-right: none; flex-grow: 1.5; }
  .feature:nth-child(3) { flex-grow: 1.6; }
  .feature svg { width: 24px; height: 24px; display: block; margin: 2px auto 4px; }

  .pets-illustration {
    position: absolute; left: 338px; top: 650px; width: 120px; height: 66px;
    border-radius: 40% 40% 10% 10%;
    background: linear-gradient(120deg, #c98b4a 0%, #e8dcc8 50%, #8d8d8d 100%);
  }

  .company-mark {
    position: absolute; right: 12px; bottom: 8px;
    display: flex; align-items: center; gap: 4px;
    font: 700 10px "Fredoka", Arial, sans-serif; color: var(--text-green);
  }
  .company-mark__dot { width: 8px; height: 8px; border-radius: 50%; background: var(--text-green); }
</style>
</head>
<body>

<span class="variant-label variant-label--a">A</span>
<span class="variant-label variant-label--b">B</span>

<!-- Variant A -->
<section class="bag bag--a">
  <div class="bag__photo" role="img" aria-label="Foto di un gattino grigio che guarda in alto su sfondo di prato verde"></div>
  <div class="bag__top"><div class="bag__handle"></div></div>

  <div class="brand-panel"><span class="brand-name">TOVA<br>NIBLO</span></div>
  <div class="claim-panel">
    <p class="claim-panel__title">LETTIERA<br>ECOLOGICA<br>PER GATTI</p>
    <p class="claim-panel__sub">e piccoli roditori</p>
  </div>

  <svg class="natural-badge" viewBox="0 0 180 66" aria-label="100% natural">
    <path d="M10 40 Q 30 6 62 14 L 150 14 Q 176 22 170 40 Q 150 60 120 56 L 30 56 Q 8 54 10 40 Z" fill="#2e8b2e"/>
    <path d="M14 40 Q 34 14 60 18" stroke="#8cc63f" stroke-width="3" fill="none"/>
    <text x="100" y="32" text-anchor="middle" font-family="Fredoka, Arial, sans-serif" font-weight="700" font-size="18" fill="#ffffff">100%</text>
    <text x="100" y="50" text-anchor="middle" font-family="Fredoka, Arial, sans-serif" font-weight="700" font-size="16" fill="#ffffff">NATURAL</text>
  </svg>

  <div class="pellet-window" role="img" aria-label="Finestra trasparente che mostra i pellet di legno"></div>

  <div class="feature-band">
    <ul class="feature-list">
      <li class="feature"><svg viewBox="0 0 24 24"><circle cx="12" cy="12" r="10" fill="none" stroke="#fff" stroke-width="1.6"/><path d="M12 6 Q16 12 12 17 Q8 12 12 6Z" fill="#fff"/></svg>Alto potere assorbente</li>
      <li class="feature"><svg viewBox="0 0 24 24"><path d="M12 3 Q19 10 17 17 Q12 22 7 17 Q5 10 12 3Z" fill="none" stroke="#fff" stroke-width="1.6"/><path d="M12 6 V19" stroke="#fff" stroke-width="1.2"/></svg>elimina gli odori</li>
      <li class="feature"><svg viewBox="0 0 24 24"><circle cx="12" cy="13" r="8" fill="none" stroke="#fff" stroke-width="1.6"/><path d="M8 13 L11 16 L16 10" stroke="#fff" stroke-width="1.6" fill="none"/></svg>biodegradabile, puoi smaltirla nel wc</li>
      <li class="feature"><svg viewBox="0 0 24 24"><path d="M3 17 Q8 14 12 17 L20 14" stroke="#fff" stroke-width="1.6" fill="none"/><circle cx="13" cy="8" r="3" fill="none" stroke="#fff" stroke-width="1.4"/></svg>economico</li>
      <li class="feature"><svg viewBox="0 0 24 24"><circle cx="12" cy="12" r="9" fill="none" stroke="#fff" stroke-width="1.6"/><path d="M12 7 V12 L15 14" stroke="#fff" stroke-width="1.6" fill="none"/></svg>lunga durata</li>
      <li class="feature"><svg viewBox="0 0 24 24"><circle cx="12" cy="15" r="4" fill="#fff"/><circle cx="6" cy="9" r="2" fill="#fff"/><circle cx="10" cy="6" r="2" fill="#fff"/><circle cx="14" cy="6" r="2" fill="#fff"/><circle cx="18" cy="9" r="2" fill="#fff"/></svg>non si attacca alle zampe</li>
    </ul>
    <div class="company-mark"><span class="company-mark__dot"></span>Foravia Nordic</div>
  </div>
  <div class="pets-illustration" role="img" aria-label="Illustrazione di coniglio, porcellino d'India e criceto"></div>
</section>

<!-- Variant B -->
<section class="bag bag--b">
  <div class="bag__photo" role="img" aria-label="Foto di un gattino grigio che guarda in alto su sfondo di prato verde"></div>
  <div class="bag__top"><div class="bag__handle"></div></div>

  <div class="brand-panel"><span class="brand-name">TOVA<br>NIBLO</span></div>
  <div class="claim-panel">
    <p class="claim-panel__title">LETTIERA<br>ECOLOGICA<br>PER GATTI</p>
    <p class="claim-panel__sub">e piccoli roditori</p>
  </div>

  <svg class="natural-badge" viewBox="0 0 180 66" aria-label="100% natural product">
    <text x="90" y="20" text-anchor="middle" font-family="Fredoka, Arial, sans-serif" font-weight="700" font-size="22" fill="#2e8b2e">100%</text>
    <rect x="42" y="25" width="96" height="22" rx="11" fill="#2e8b2e"/>
    <text x="90" y="42" text-anchor="middle" font-family="Fredoka, Arial, sans-serif" font-weight="700" font-size="16" fill="#ffffff">NATURAL</text>
    <rect x="58" y="49" width="64" height="15" rx="7" fill="#8cc63f"/>
    <text x="90" y="60" text-anchor="middle" font-family="Fredoka, Arial, sans-serif" font-weight="500" font-size="10" fill="#ffffff">PRODUCT</text>
    <path d="M30 36 Q36 28 42 34" stroke="#8cc63f" stroke-width="3" fill="none"/>
    <path d="M138 34 Q144 28 150 36" stroke="#8cc63f" stroke-width="3" fill="none"/>
  </svg>

  <div class="pellet-window" role="img" aria-label="Finestra trasparente che mostra i pellet di legno"></div>

  <div class="feature-band">
    <ul class="feature-list">
      <li class="feature"><svg viewBox="0 0 24 24"><circle cx="12" cy="12" r="10" fill="none" stroke="#fff" stroke-width="1.6"/><path d="M12 6 Q16 12 12 17 Q8 12 12 6Z" fill="#fff"/></svg>Alto potere assorbente</li>
      <li class="feature"><svg viewBox="0 0 24 24"><path d="M12 3 Q19 10 17 17 Q12 22 7 17 Q5 10 12 3Z" fill="none" stroke="#fff" stroke-width="1.6"/><path d="M12 6 V19" stroke="#fff" stroke-width="1.2"/></svg>elimina gli odori</li>
      <li class="feature"><svg viewBox="0 0 24 24"><circle cx="12" cy="13" r="8" fill="none" stroke="#fff" stroke-width="1.6"/><path d="M8 13 L11 16 L16 10" stroke="#fff" stroke-width="1.6" fill="none"/></svg>biodegradabile, puoi smaltirla nel wc</li>
      <li class="feature"><svg viewBox="0 0 24 24"><path d="M3 17 Q8 14 12 17 L20 14" stroke="#fff" stroke-width="1.6" fill="none"/><circle cx="13" cy="8" r="3" fill="none" stroke="#fff" stroke-width="1.4"/></svg>economico</li>
      <li class="feature"><svg viewBox="0 0 24 24"><circle cx="12" cy="12" r="9" fill="none" stroke="#fff" stroke-width="1.6"/><path d="M12 7 V12 L15 14" stroke="#fff" stroke-width="1.6" fill="none"/></svg>lunga durata</li>
      <li class="feature"><svg viewBox="0 0 24 24"><circle cx="12" cy="15" r="4" fill="#fff"/><circle cx="6" cy="9" r="2" fill="#fff"/><circle cx="10" cy="6" r="2" fill="#fff"/><circle cx="14" cy="6" r="2" fill="#fff"/><circle cx="18" cy="9" r="2" fill="#fff"/></svg>non si attacca alle zampe</li>
    </ul>
    <div class="company-mark"><span class="company-mark__dot"></span>Foravia Nordic</div>
  </div>
  <div class="pets-illustration" role="img" aria-label="Illustrazione di coniglio, porcellino d'India e criceto"></div>
</section>

</body>
</html>
```